Design for Outdoor Sign/Banner to be used at Markets/Pop Up Events

We are a small boutique nursery based in Brindle Creek, QLD specialising in Platycerium species. We propagate, grow and sell the 18 different species of Platycerium. All of our Platyceriums are grown in shade houses on site and are hardened in natural conditions. We would like to see designs that use the colour green. I will attach our Company Logo and also the Stubbie Cooler Design that a designer created through Motif Harbour. Banner size would be approx 2 metres wide, 1 metre high.

```html
<!DOCTYPE html>
<html lang="en">
<head>
<meta charset="utf-8">
<title>Boutique Nursery Banner</title>
<link href="https://fonts.googleapis.com/css2?family=Montserrat:wght@800;900&family=Poppins:wght@500;600;700&family=Allura&display=swap" rel="stylesheet">
<style>
  :root {
    --stage: #9ba38b;
    --leaf: #74b11c;
    --leaf-soft: #82bd2a;
    --forest: #0f4d12;
    --band-dark: #165f12;
    --band-mid: #1d7417;
    --white: #ffffff;
    --ink: #1b1b1b;
    --photo-a: #8a6f62;
    --photo-b: #9cc74a;
  }
  * { margin: 0; padding: 0; box-sizing: border-box; }
  html, body { width: 800px; height: 1200px; overflow: hidden; }
  body { background: var(--stage); position: relative; font-family: "Poppins", sans-serif; }

  .banner {
    position: absolute; left: 50px; top: 425px; width: 700px; height: 350px;
    background: var(--white); overflow: hidden;
    box-shadow: 0 6px 14px rgba(0,0,0,.18);
  }
  .hero {
    position: absolute; left: 0; top: 0; width: 515px; height: 176px;
    background: linear-gradient(135deg, var(--leaf-soft), var(--leaf));
  }
  .headline {
    position: absolute; left: 33px; top: 10px;
    font-family: "Montserrat", sans-serif; font-weight: 900; line-height: .92;
  }
  .headline .word-boutique { display: block; color: var(--white); font-size: 60px; letter-spacing: -1px; }
  .headline .word-nursery { display: block; color: var(--forest); font-size: 64px; letter-spacing: -1px; }
  .tagline {
    position: absolute; left: 32px; top: 118px; color: var(--white); white-space: nowrap;
  }
  .tagline .script { font-family: "Allura", cursive; font-size: 44px; vertical-align: -6px; }
  .tagline .caps { font-family: "Montserrat", sans-serif; font-weight: 800; font-size: 30px; letter-spacing: -.5px; }

  .photo {
    position: absolute; left: 375px; top: 30px; width: 325px; height: 318px;
    background: linear-gradient(160deg, var(--photo-a) 0%, #7b5f52 45%, var(--photo-b) 100%);
    border-radius: 6px;
  }

  .features {
    position: absolute; left: 0; top: 176px; width: 515px; height: 72px;
    display: flex;
  }
  .feature {
    position: relative; height: 100%; color: var(--white);
    display: flex; align-items: center; justify-content: center; text-align: center;
    font-size: 10.5px; font-weight: 500; line-height: 1.2; padding-top: 14px;
  }
  .feature:nth-child(odd) { background: var(--band-dark); }
  .feature:nth-child(even) { background: var(--band-mid); }
  .feature .badge {
    position: absolute; top: -14px; left: 50%; transform: translateX(-50%);
    width: 30px; height: 30px; border-radius: 50%; background: var(--white);
    border: 3px solid var(--band-mid); display: flex; align-items: center; justify-content: center;
  }
  .feature .badge svg { width: 17px; height: 17px; }

  .contact { position: absolute; left: 0; top: 248px; width: 380px; height: 102px; }
  .brand-mark {
    position: absolute; left: 33px; top: 16px; width: 62px;
    font-family: "Poppins", sans-serif; font-weight: 700; font-size: 12px;
    color: var(--forest); line-height: 1.15; text-align: center;
  }
  .brand-mark .box {
    display: block; width: 14px; height: 14px; background: var(--forest); margin: 0 auto 5px;
  }
  .visit {
    position: absolute; left: 114px; top: 9px; white-space: nowrap;
    font-family: "Montserrat", sans-serif; font-weight: 800; font-size: 14.5px; color: var(--ink);
  }
  .visit .accent { color: var(--band-mid); }
  .details {
    position: absolute; left: 116px; top: 33px; white-space: nowrap;
    display: flex; gap: 12px; align-items: center;
    font-weight: 600; font-size: 14.5px; color: var(--ink);
  }
  .details span { display: inline-flex; align-items: center; gap: 6px; }
  .details svg { width: 15px; height: 15px; }
  .follow {
    position: absolute; left: 115px; top: 58px; width: 378px; height: 19px;
    border: 1px solid #bdbdbd; border-radius: 5px; display: flex; align-items: center;
    font-size: 10.5px; white-space: nowrap;
  }
  .follow .pill {
    background: var(--leaf); color: var(--white); font-weight: 600; font-size: 12px;
    height: 19px; margin: -1px 0 -1px -1px; padding: 0 10px; border-radius: 5px;
    display: flex; align-items: center;
  }
  .follow .url { padding-left: 9px; letter-spacing: .6px; color: var(--ink); }
  .follow .url b { font-weight: 700; }
</style>
</head>
<body>
  <section class="banner">
    <div class="hero">
      <h1 class="headline">
        <span class="word-boutique">BOUTIQUE</span>
        <span class="word-nursery">NURSERY</span>
      </h1>
      <p class="tagline"><span class="script">Unique</span> <span class="caps">PLATYCERIUMS</span></p>
    </div>

    <div class="photo" role="img" aria-label="Staghorn ferns mounted on shield-shaped wooden boards hanging from a rusted mesh"></div>

    <ul class="features">
      <li class="feature" style="width:112px">
        <span class="badge"><svg viewBox="0 0 20 20" fill="none" stroke="#1d7417" stroke-width="1.6"><path d="M4 16 L16 4"/><path d="M10 10 L5 6 M12 8 L14 12 M8 12 L9 17"/></svg></span>
        18 Distinct<br>Species of<br>Platycerium
      </li>
      <li class="feature" style="width:99px">
        <span class="badge"><svg viewBox="0 0 20 20" fill="none" stroke="#1d7417" stroke-width="1.6"><path d="M6 12 h8 l-1 6 h-6 z"/><path d="M10 12 V5 M10 8 C7 7 6 5 6 4 M10 7 C13 6 14 4 14 3"/></svg></span>
        Locally<br>Propagated &amp;<br>Grown on Site
      </li>
      <li class="feature" style="width:83px">
        <span class="badge"><svg viewBox="0 0 20 20" fill="none" stroke="#1d7417" stroke-width="1.6"><path d="M3 14 C7 13 9 17 15 14 L17 12"/><path d="M10 12 V6 M10 8 C8 7 7 5 7 4 M10 7 C12 6 13 5 13 3"/></svg></span>
        Hardened<br>in Natural<br>Conditions
      </li>
      <li class="feature" style="width:99px">
        <span class="badge"><svg viewBox="0 0 20 20" fill="none" stroke="#1d7417" stroke-width="1.6"><path d="M3 9 L10 3 L17 9 V17 H3 Z"/><path d="M7 11 V15 M10 11 V15 M13 11 V15"/></svg></span>
        Specialized<br>Shade House<br>Cultivation
      </li>
      <li class="feature" style="width:122px">
        <span class="badge"><svg viewBox="0 0 20 20" fill="none" stroke="#1d7417" stroke-width="1.6"><path d="M3 16 V8 C3 5 17 5 17 8 V16 Z"/><path d="M7 16 V11 H11 V16"/></svg></span>
        Boutique<br>Nursery in<br>Brindle Creek, QLD
      </li>
    </ul>

    <div class="contact">
      <div class="brand-mark"><span class="box"></span>FERNVALE STAGHORNS</div>
      <p class="visit"><span class="accent">VISIT US</span> TO EXPLORE OUR UNIQUE COLLECTION!</p>
      <p class="details">
        <span><svg viewBox="0 0 24 24" fill="#1d7417"><path d="M6.6 10.8a15 15 0 0 0 6.6 6.6l2.2-2.2a1 1 0 0 1 1-.25 11.4 11.4 0 0 0 3.6.57 1 1 0 0 1 1 1V20a1 1 0 0 1-1 1A17 17 0 0 1 3 4a1 1 0 0 1 1-1h3.5a1 1 0 0 1 1 1c0 1.25.2 2.45.57 3.57a1 1 0 0 1-.25 1z"/></svg>0400 555 218</span>
        <span><svg viewBox="0 0 24 24" fill="#74b11c"><path d="M12 2a7 7 0 0 0-7 7c0 5.2 7 13 7 13s7-7.8 7-13a7 7 0 0 0-7-7zm0 9.5A2.5 2.5 0 1 1 12 6.5a2.5 2.5 0 0 1 0 5z"/></svg>Brindle Creek, QLD, Australia, 4599</span>
      </p>
      <p class="follow"><span class="pill">Follow us</span><span class="url">https://www.<b>fernvalestaghorns</b>.com.au</span></p>
    </div>
  </section>
</body>
</html>
```